Flyer für ein Onlineportal für private Vermieter
Design hat direkt unseren Geschmack getroffen.
Zielgruppe
Onlineportal für private Vermieter. Zentrale Botschaft: Mieterhöhungen sind in Orten ohne Mietspiegel fast unmöglich. Die Lösung? Ortsübliche Vergleichsmieten. Unsere Plattform bietet Zugang zu ortsüblichen Vergleichsmieten.
Aufgabenstellung
Stock-Bilder bitte von Velmora Bildarchiv, weil wir hier ein Abonnement haben.

```html
<!DOCTYPE html>
<html lang="de">
<head>
<meta charset="utf-8">
<title>Nachhaltig vermieten – Flyer</title>
<link rel="stylesheet" href="https://fonts.googleapis.com/css2?family=Montserrat:wght@400;500;700;800&display=swap">
<style>
:root{
  --blue:#1ea9e1;
  --blue-dark:#0a8fd0;
  --black:#111111;
  --grey-band:#e3e4e6;
  --ink:#1c1c1c;
  --stage:#a9aeae;
  --white:#ffffff;
  --navy:#1a2b48;
}
*{box-sizing:border-box;margin:0;padding:0}
html,body{width:1200px;height:2352px;overflow:hidden}
body{background:var(--stage);font-family:"Montserrat",sans-serif;color:var(--ink)}
.flyer{position:absolute;left:50px;top:400px;width:1100px;height:1552px;background:var(--white);overflow:hidden}
.header{position:absolute;left:0;top:0;width:100%;height:184px;background:linear-gradient(180deg,var(--blue) 0%,var(--blue-dark) 100%);text-align:center;color:var(--white)}
.header h1{font-weight:800;font-size:72px;letter-spacing:0.5px;line-height:1;padding-top:40px}
.header h2{font-weight:800;font-size:36px;line-height:1;margin-top:8px}
.intro{position:absolute;left:0;top:184px;width:100%;height:142px;background:var(--grey-band);display:flex;align-items:center;justify-content:center;text-align:center;font-size:19.5px;line-height:26px;padding:0 70px}
.middle-shapes{position:absolute;left:0;top:326px;width:1100px;height:590px}
.brand{position:absolute;left:295px;top:380px;display:flex;align-items:center;gap:14px}
.brand-square{width:44px;height:44px;background:var(--blue)}
.brand-name{font-weight:700;font-size:36px;color:var(--black)}
.feature{position:absolute;left:84px;top:505px;width:600px;text-align:center}
.feature h3{font-weight:700;font-size:34px;line-height:45px;color:var(--blue);white-space:nowrap}
.feature p{font-size:20.5px;line-height:26px;margin-top:12px;white-space:nowrap}
.why-bar{position:absolute;left:0;top:912px;width:100%;height:104px;background:var(--black);border-bottom:17px solid var(--blue);display:flex;align-items:center;justify-content:center}
.why-bar h3{color:var(--white);font-weight:800;font-size:36px;margin-top:-6px}
.body-copy{position:absolute;left:60px;top:1058px;width:980px;text-align:center;font-size:20.5px;line-height:26px}
.body-copy p+p{margin-top:19px}
.footer-shapes{position:absolute;left:0;top:1360px;width:1100px;height:192px}
.footer-url{position:absolute;left:0;top:1480px;width:100%;text-align:center;color:var(--white);font-weight:700;font-size:25px;letter-spacing:4.5px}
</style>
</head>
<body>
<main class="flyer">
  <header class="header">
    <h1>NACHHALTIG VERMIETEN</h1>
    <h2>PRIVATVERMIETER SIND KEINE MIETKONZERNE.</h2>
  </header>

  <section class="intro">
    <p>Steigende Kosten für Baustoffe und Handwerker bei Sanierung oder Renovierung machen in vielen Fällen eine Erhöhung der Miete leider erforderlich. Dabei geht es nicht um Gewinnmaximierung - privates Vermieten droht immer mehr zum Draufzahlgeschäft zu werden.</p>
  </section>

  <svg class="middle-shapes" viewBox="0 0 1100 590">
    <defs>
      <linearGradient id="panel-fade" x1="0" y1="0" x2="1" y2="1">
        <stop offset="0" stop-color="#ffffff"/>
        <stop offset="1" stop-color="#f1f2f3"/>
      </linearGradient>
      <radialGradient id="photo-tone" cx="0.6" cy="0.5" r="0.7">
        <stop offset="0" stop-color="#3a5580"/>
        <stop offset="0.6" stop-color="#1a2b48"/>
        <stop offset="1" stop-color="#0d1628"/>
      </radialGradient>
    </defs>
    <rect x="0" y="0" width="1100" height="590" fill="url(#panel-fade)"/>
    <polygon points="0,24 131,24 0,586" fill="#111111"/>
    <polygon role="img" aria-label="Foto: Geschäftsmann im Anzug hält schützend die Hände um ein leuchtendes Haussymbol" points="716,24 1100,24 1100,560 618,560" fill="url(#photo-tone)"/>
  </svg>

  <div class="brand">
    <span class="brand-square"></span>
    <span class="brand-name">Vermieterkreis</span>
  </div>

  <section class="feature">
    <h3>Der Staat lässt private<br>Vermieter im Regen stehen</h3>
    <p>Für Mietkonzerne ist es in der Regel kein<br>Problem ausreichend Ver-gleichsmieten<br>vorzuweisen, denn diese verfügen<br>normalerweise selbst über ausreichend<br>Immobilien die genutzt werden können.</p>
    <p>Private Vermieter jedoch, haben in Regionen<br>ohne Mietspiegel nahezu keine Möglichkeit<br>eine Mieterhöhung durchzusetzen - trotz<br>steigender gesetzlicher Anforderungen<br>an bestehendem Wohnraum.</p>
  </section>

  <div class="why-bar">
    <h3>Warum ist es wichtig, dass Vermieten rentabel ist?</h3>
  </div>

  <section class="body-copy">
    <p>Private Vermietung ist eine soziale Investition. Menschen investieren Ihr Geld in Wohnraum<br>für andere. Das passiert allerdings nur, wenn man damit keine Verluste macht.</p>
    <p>Ist dies nicht mehr der Fall, erfolgt oft der Verkauf an Investoren. Das Problem dabei ist, dass<br>diese oft nur an der Wertentwicklung der Immobilie interessiert sind. Häufig stehen diese<br>Wohnungen leer oder werden luxussaniert für einen Weiterverkauf.</p>
    <p>Wohnraum wird damit verknappt und der Druck am Wohnungsmarkt erhöht sich. Eine<br>Entwicklung die gesellschaftlich problematisch ist.</p>
    <p>Dies lässt sich nur verhindern, wenn Vermieter einen angemessenen Mietzins fordern bzw.<br>erhalten. Dies liegt gleichermaßen im Interesse von Mietern und Vermietern. Nur so ist<br>Vermietung auch nachhaltig.</p>
  </section>

  <svg class="footer-shapes" viewBox="0 0 1100 192" aria-hidden="true">
    <path d="M0 0 Q560 110 1100 8 L1100 192 L0 192 Z" fill="#111111"/>
    <path d="M0 42 Q560 118 1100 40 L1100 192 L0 192 Z" fill="#1ea9e1"/>
  </svg>
  <p class="footer-url">www.mietwertportal.de</p>
</main>
</body>
</html>
```